Clean and modern business cards

Looking for an updated business card design for my dental office “corvanta dental” . Looking for a modern clean / sleek design . I’m thinking black background but open to seeing other options . One side needs to have an appointment card . Card needs to have logo, dentist name , phone, email , address . I’ve attached couple of cards I thought were cool as well as my logo
Target Market(s)
Dental patients
Industry/Entity Type
Dentistry
Contact Information for Business Card
Phone email address

```html
<!DOCTYPE html>
<html lang="en">
<head>
<meta charset="utf-8">
<title>Corvanta Dental – Business Card</title>
<link href="https://fonts.googleapis.com/css2?family=Montserrat:wght@400;500;800&display=swap" rel="stylesheet">
<style>
  :root {
    --bg: #c9c9c9;
    --card: #ffffff;
    --ink: #111111;
    --muted: #444444;
    --rule: #555555;
    --accent: #f2b705;
  }
  * { box-sizing: border-box; margin: 0; padding: 0; }
  html, body { width: 1200px; height: 900px; overflow: hidden; }
  body {
    background: var(--bg);
    font-family: "Montserrat", Arial, sans-serif;
    color: var(--ink);
    display: flex;
    align-items: center;
    justify-content: center;
    gap: 44px;
  }
  .card {
    width: 540px;
    height: 308px;
    background: var(--card);
    border-radius: 22px;
    position: relative;
    box-shadow: 0 6px 18px rgba(0,0,0,.18);
  }

  /* Appointment side */
  .appointment { padding: 30px 36px; }
  .appointment__title {
    text-align: center;
    font-weight: 800;
    font-size: 20px;
    letter-spacing: .5px;
    margin-bottom: 18px;
  }
  .field-row { display: flex; align-items: flex-end; gap: 6px; font-size: 14px; margin-bottom: 14px; }
  .field-row .line { flex: 1; border-bottom: 1.5px dotted var(--rule); height: 14px; }
  .field-row .label { white-space: nowrap; }
  .days { display: flex; justify-content: space-between; font-size: 14px; margin: 4px 0 16px; }
  .day { display: flex; align-items: center; gap: 6px; }
  .day .box { width: 20px; height: 15px; border: 2px solid var(--ink); }
  .note-line { border-bottom: 1.5px dotted var(--rule); height: 16px; margin-bottom: 10px; }
  .policy { text-align: center; font-size: 10.5px; line-height: 1.4; color: var(--muted); margin-top: 6px; }

  /* Contact side */
  .contact { padding: 40px 38px; }
  .brand { display: flex; align-items: center; gap: 16px; }
  .brand__mark { width: 52px; height: 52px; border-radius: 50%; background: var(--accent); flex: none; }
  .brand__name { font-weight: 800; font-size: 31px; letter-spacing: .5px; text-transform: uppercase; line-height: 1; }
  .person { position: absolute; left: 38px; bottom: 34px; }
  .person__name { font-weight: 800; font-size: 22px; text-transform: uppercase; }
  .person__role { font-size: 15px; margin-bottom: 12px; }
  .contact-list { list-style: none; font-size: 14px; line-height: 1.7; }
  .contact-list li { display: flex; align-items: center; gap: 10px; }
  .contact-list svg { width: 16px; height: 16px; flex: none; }
  .web-accent { color: var(--accent); }
  .address {
    position: absolute; right: 36px; bottom: 38px;
    text-align: right; font-size: 14px; line-height: 1.45;
  }
</style>
</head>
<body>

<section class="card appointment" aria-label="Appointment card">
  <h2 class="appointment__title">NEXT APPOINTMENT</h2>
  <div class="field-row"><span class="line"></span><span class="label">has an appointment</span></div>
  <div class="field-row">
    <span class="label">Date</span><span class="line"></span>
    <span class="label">Time</span><span class="line"></span>
    <span class="label">AM/PM</span>
  </div>
  <div class="days">
    <span class="day"><span class="box"></span>Mon</span>
    <span class="day"><span class="box"></span>Tue</span>
    <span class="day"><span class="box"></span>Wed</span>
    <span class="day"><span class="box"></span>Thu</span>
    <span class="day"><span class="box"></span>Fri</span>
    <span class="day"><span class="box"></span>Sat</span>
  </div>
  <div class="field-row"><span class="label">Note</span><span class="line"></span></div>
  <div class="note-line"></div>
  <p class="policy">Please give me 24 hours notice if you are unable to keep your<br>appointment or a cancellation fee may be charged</p>
</section>

<section class="card contact" aria-label="Contact card">
  <div class="brand">
    <span class="brand__mark"></span>
    <span class="brand__name">Corvanta Dental</span>
  </div>

  <div class="person">
    <p class="person__name">Marcus Hale</p>
    <p class="person__role">Managing Director</p>
    <ul class="contact-list">
      <li>
        <svg viewBox="0 0 24 24" aria-hidden="true"><path fill="#f2b705" d="M6.6 10.8a15 15 0 0 0 6.6 6.6l2.2-2.2c.3-.3.7-.4 1-.2 1.1.4 2.3.6 3.6.6.6 0 1 .4 1 1V20c0 .6-.4 1-1 1A17 17 0 0 1 3 4c0-.6.4-1 1-1h3.5c.6 0 1 .4 1 1 0 1.3.2 2.5.6 3.6.1.3 0 .7-.2 1z"/></svg>
        044-555 210 873
      </li>
      <li>
        <svg viewBox="0 0 24 24" aria-hidden="true"><rect x="2" y="5" width="20" height="14" fill="#f2b705"/><path d="M2 5l10 8 10-8" fill="none" stroke="#fff" stroke-width="1.6"/></svg>
        hello@corvantadental.com
      </li>
      <li>
        <svg viewBox="0 0 24 24" aria-hidden="true"><g fill="none" stroke="#f2b705" stroke-width="2"><circle cx="12" cy="12" r="9"/><ellipse cx="12" cy="12" rx="4" ry="9"/><path d="M3 12h18"/></g></svg>
        <span>www.<span class="web-accent">corvantadental</span>.com</span>
      </li>
    </ul>
  </div>

  <p class="address">87 Linden Row, Suite 4<br>30718, Harbor City</p>
</section>

</body>
</html>
```